Banner Design 4040mm W x 2190mm H

Design a glamorous and exciting 4040mm W x 2190mm H backdrop for the QRLMT Velvet Orchid Gala at the luxurious Tallow Hall, Fenwick, Mirrabelle, Sydney. This exciting backdrop should be spectacular so that people will be excited to take photos in front of it.
Design Colours preferred is black and pink.
Please include our website on the banner www.qrlmt.org.au
Should include the words "QRLMT Velvet Orchid Gala" as the main attraction on the banner.
Please include "Thank you to our sponsors" and include the logo of the sponsors.
Sponsors:
Brockden Pathology
EastGlen Radiology
KTV Diagnostic Imaging
Harbin Legal Group
Truffords
Banner Template:
4040mm W x 2190mm H Single Sided (.AI)
https://files.example-share.net/d/8ZkQm3TnWp47LcVbXr2YhJd5Fs61Ae/view
QRLMT Logo:
Can be obtained from our website www.qrlmt.org.au

```html
<!DOCTYPE html>
<html lang="en">
<head>
<meta charset="utf-8">
<title>QRLMT Velvet Orchid Gala – Backdrop</title>
<link rel="stylesheet" href="https://fonts.googleapis.com/css2?family=Abril+Fatface&family=Great+Vibes&display=swap">
<style>
  :root {
    --stage: #0d111c;
    --magenta-deep: #6e0f45;
    --magenta: #9c1c63;
    --magenta-bright: #c42a82;
    --script-pink: #d0358e;
    --cream: #f3e4cf;
    --gold: #c9a77a;
    --ink: #3a2b3a;
    --white: #ffffff;
  }
  * { margin: 0; padding: 0; box-sizing: border-box; }
  html, body {
    width: 1200px; height: 729px; overflow: hidden;
    background: var(--stage);
  }
  .canvas { position: relative; width: 1200px; height: 729px; background: var(--stage); }
  .backdrop {
    position: absolute; left: 37px; top: 58px; width: 1129px; height: 604px;
    overflow: hidden;
    background:
      radial-gradient(ellipse at 70% 45%, var(--magenta-bright) 0%, var(--magenta) 45%, var(--magenta-deep) 100%);
  }
  .backdrop__pattern {
    position: absolute; inset: 0;
    background: linear-gradient(160deg, rgba(255,255,255,0.05), rgba(0,0,0,0.12));
  }
  .backdrop__shards { position: absolute; inset: 0; width: 100%; height: 100%; }
  .title-frame {
    position: absolute; left: 20px; top: 120px; width: 1095px; height: 276px;
    border: 3px solid var(--gold);
    box-shadow: 0 0 8px rgba(255,230,190,0.5);
  }
  .title { position: absolute; inset: 0; font-weight: normal; }
  .title__org, .title__rest {
    position: absolute; font-family: "Abril Fatface", serif; color: var(--cream);
    font-size: 60px; line-height: 1; letter-spacing: 1px; white-space: nowrap;
    text-shadow: 0 2px 3px rgba(60,0,30,0.5);
  }
  .title__org { left: 36px; top: 232px; }
  .title__rest { left: 637px; top: 232px; }
  .title__script {
    position: absolute; left: 150px; top: 70px;
    padding: 0 40px;
    font-family: "Great Vibes", cursive; font-size: 260px; line-height: 1.1;
    white-space: nowrap; overflow: visible;
    color: var(--script-pink);
    text-shadow: 0 3px 6px rgba(70,0,40,0.35);
  }
  .website {
    position: absolute; left: 28px; top: 568px;
    font-family: "Abril Fatface", serif; font-size: 16px; color: var(--cream);
    letter-spacing: 1px;
  }
  .sponsors-heading {
    position: absolute; left: 655px; top: 462px;
    font-family: "Great Vibes", cursive; font-size: 50px; color: var(--white); line-height: 1.2;
    white-space: nowrap; font-weight: normal;
  }
  .host-mark {
    position: absolute; left: 626px; top: 536px; width: 66px;
    display: flex; flex-direction: column; align-items: center; gap: 4px;
    font-family: "Abril Fatface", serif; font-size: 11px; color: var(--cream);
  }
  .host-mark__dot { width: 18px; height: 18px; border-radius: 50%; background: var(--cream); }
  .sponsor-strip {
    position: absolute; left: 700px; top: 538px; width: 394px; height: 43px;
    background: var(--white); list-style: none;
    display: flex; align-items: center; padding: 0 4px;
  }
  .sponsor-strip__name {
    flex: 1 1 0; list-style: none;
    font-family: "Abril Fatface", serif; font-size: 9.5px; color: var(--ink);
    text-align: center; line-height: 1.15; padding: 0 3px;
  }
</style>
</head>
<body>
<main class="canvas">
  <section class="backdrop">
    <div class="backdrop__pattern" role="img" aria-label="Tonal magenta floral damask pattern"></div>
    <svg class="backdrop__shards" viewBox="0 0 1129 604" aria-hidden="true">
      <polygon points="130,0 240,0 40,604 0,604 0,480" fill="rgba(40,0,25,0.35)"/>
      <polygon points="300,0 560,0 330,604 250,604" fill="rgba(255,255,255,0.06)"/>
      <polygon points="520,40 600,0 380,604 340,604" fill="rgba(30,0,20,0.45)"/>
      <polygon points="0,150 210,520 150,604 0,604" fill="rgba(255,255,255,0.05)"/>
      <polygon points="200,0 260,0 300,280 250,300" fill="rgba(20,0,15,0.35)"/>
    </svg>
    <div class="title-frame"></div>
    <h1 class="title">
      <span class="title__org">QRLMT</span>
      <span class="title__script">Velvet</span>
      <span class="title__rest">Orchid Gala</span>
    </h1>
    <p class="website">www.qrlmt.org.au</p>
    <p class="sponsors-heading">Thank You to our sponsors</p>
    <div class="host-mark"><span class="host-mark__dot"></span>QRLMT</div>
    <ul class="sponsor-strip">
      <li class="sponsor-strip__name">Truffords</li>
      <li class="sponsor-strip__name">KTV Diagnostic Imaging</li>
      <li class="sponsor-strip__name">EastGlen Radiology</li>
      <li class="sponsor-strip__name">Harbin Legal Group</li>
      <li class="sponsor-strip__name">Brockden Pathology</li>
    </ul>
  </section>
</main>
</body>
</html>
```